Vimcarra, Cosmetic skin care line

I am not looking to change my logo vimcarra on the label just want someone to design a different label I want it to be very classy as it is already just want something different. My product target classier people and people with higher income and for woman and men but mostly women. Looking to keep the label background black

Target Market(s)

Classier and higer income women/men mostly women

Industry/Entity Type

Cosmetics

• I don't really know

Colors

Designer to choose colors to be used in the design.

Requirements
Must have
• It must keep the same vimcarra logo and the same matte black background color
Nice to have
• I want a different layout and maybe different fonts for the label
Should not have

```html
<!DOCTYPE html>
<html lang="en">
<head>
<meta charset="utf-8">
<title>Vimcarra Eye Corrector Serum – Label</title>
<link rel="stylesheet" href="https://fonts.googleapis.com/css2?family=Josefin+Sans:wght@300;400&display=swap">
<style>
  :root {
    --backdrop: #e6e6e6;
    --label-black: #000000;
    --ink-white: #ffffff;
  }
  * { margin: 0; padding: 0; box-sizing: border-box; }
  html, body {
    width: 1200px;
    height: 959px;
    overflow: hidden;
    background: var(--backdrop);
  }
  .canvas {
    position: relative;
    width: 1200px;
    height: 959px;
    display: flex;
    align-items: center;
    justify-content: center;
  }
  .label {
    position: relative;
    width: 621px;
    height: 820px;
    background: var(--label-black);
    color: var(--ink-white);
    font-family: "Josefin Sans", sans-serif;
    text-align: center;
  }
  .label > * {
    position: absolute;
    left: 0;
    right: 0;
    line-height: 1;
  }
  .brand-name {
    top: 176px;
    font-size: 72px;
    font-weight: 400;
    letter-spacing: 0.14em;
    padding-left: 0.14em;
  }
  .brand-tagline {
    top: 282px;
    font-size: 26px;
    font-weight: 300;
    letter-spacing: 0.3em;
    padding-left: 0.3em;
  }
  .product-line {
    top: 398px;
    font-size: 54px;
    font-weight: 300;
    letter-spacing: 0.02em;
  }
  .product-name {
    top: 452px;
    font-size: 128px;
    font-weight: 300;
    letter-spacing: 0.03em;
  }
  .product-note {
    top: 730px;
    font-size: 22px;
    font-weight: 300;
    letter-spacing: 0.04em;
  }
</style>
</head>
<body>
  <main class="canvas">
    <section class="label" aria-label="Vimcarra Eye Corrector Serum label">
      <h1 class="brand-name">VIMCARRA</h1>
      <p class="brand-tagline">FOR ALL</p>
      <p class="product-line">EYE CORRECTOR</p>
      <h2 class="product-name">SERUM</h2>
      <p class="product-note">WITH TRIPLE PEPTIDES</p>
    </section>
  </main>
</body>
</html>
```